Theo Brandvik Photography
Theo Brandvik Photography's Homepage
Photography
Professional photographer
top
Overall look and feel should come from logo design.

```html
<!DOCTYPE html>
<html lang="en">
<head>
<meta charset="utf-8">
<title>Theo Brandvik Photography</title>
<link href="https://fonts.googleapis.com/css2?family=PT+Sans:ital,wght@0,400;0,700;1,400;1,700&display=swap" rel="stylesheet">
<style>
  :root{
    --page:#ebebeb;
    --panel:#ffffff;
    --panel-line:#dcdcdc;
    --ink:#333333;
    --muted:#555555;
    --accent-green:#8cbf26;
    --accent-yellow:#f5c400;
    --accent-red:#c8161d;
    --accent-red-dark:#8e0f14;
    --thumb:#3a3a3a;
    --footer:#1f1f1f;
    --footer-text:#cfcfcf;
  }
  *{box-sizing:border-box;margin:0;padding:0}
  html,body{width:1200px;height:1055px;overflow:hidden}
  body{background:var(--page);font-family:"PT Sans",Arial,sans-serif;color:var(--ink);position:relative}

  .masthead{position:absolute;left:0;top:0;width:1200px;height:180px;
    background:linear-gradient(180deg,#9a9a9a 0%,#6e6e6e 45%,#4a4a4a 100%)}
  .masthead-rule{position:absolute;left:0;top:180px;width:1200px;height:6px;background:var(--accent-yellow)}
  .brand{position:absolute;left:0;top:22px;width:365px;height:110px;background:#fff;
    display:flex;align-items:center;padding-left:22px;gap:14px;box-shadow:0 2px 6px rgba(0,0,0,.3)}
  .brand-mark{width:54px;height:54px;background:var(--ink)}
  .brand-name{font-size:30px;font-weight:700;color:var(--ink);line-height:1;width:250px}
  .slogan{position:absolute;left:500px;top:72px;width:480px;text-align:center;color:#fff;
    font-size:36px;font-weight:700;text-shadow:0 2px 4px rgba(0,0,0,.5)}
  .slogan em{font-style:normal;color:var(--accent-yellow)}
  .main-nav{position:absolute;right:0;top:0;height:43px;background:#fff;display:flex;align-items:center;padding-right:8px}
  .main-nav a{font-size:16px;color:var(--ink);text-decoration:none;padding:0 10px;line-height:43px}
  .main-nav a.current{background:var(--accent-red);color:#fff;border-bottom:4px solid var(--accent-red-dark);line-height:39px;padding:0 14px}

  .panel{position:absolute;background:var(--panel);border:1px solid var(--panel-line);border-radius:4px}
  .intro{left:130px;top:222px;width:925px;height:305px}
  .feature{position:absolute;left:30px;top:26px;width:587px;height:257px;
    background:linear-gradient(180deg,#e6e6e6 0%,#bdbdbd 60%,#8f8f8f 100%);box-shadow:3px 3px 5px rgba(0,0,0,.35)}
  .feature-caption{position:absolute;left:0;right:0;top:160px;text-align:center;
    font-size:20px;font-style:italic;font-weight:700;color:#222;letter-spacing:.5px}
  .welcome{position:absolute;left:635px;top:30px;width:270px}
  h2{font-size:21px;font-weight:700;color:var(--accent-green)}
  .welcome p{margin-top:14px;font-size:14px;line-height:17px;color:var(--muted);text-align:justify}
  .signature{text-align:right;margin-top:14px;font-style:italic;font-size:15px;color:var(--muted)}

  .latest{left:130px;top:547px;width:602px;height:299px}
  .latest h2{position:absolute;left:26px;top:18px}
  .thumb{position:absolute;top:70px;width:151px;text-align:center}
  .thumb-frame{height:157px;background:var(--thumb);border:4px solid #d6d6d6;
    display:flex;align-items:center;justify-content:center;color:#fff;font-size:14px}
  .thumb span{display:block;margin-top:10px;font-size:12px;color:var(--ink)}

  .about{left:761px;top:547px;width:294px;height:299px}
  .about h2{position:absolute;left:16px;top:18px}
  .portrait{position:absolute;left:16px;top:48px;width:250px;height:103px;background:var(--thumb);
    border:4px solid #d6d6d6;display:flex;align-items:center;justify-content:center;color:#fff;font-size:14px}
  .about p{position:absolute;left:16px;top:162px;width:256px;font-size:13.5px;line-height:15.5px;color:var(--muted);text-align:justify}
  .about p a{color:var(--accent-red);text-decoration:none}

  .site-footer{position:absolute;left:0;top:955px;width:1200px;height:100px;background:var(--footer);border-top:3px solid #333}
  .elsewhere{position:absolute;left:26px;top:34px;color:var(--footer-text)}
  .elsewhere strong{display:block;font-size:16px;font-weight:400}
  .elsewhere small{font-size:10px}
  .footer-nav{position:absolute;left:0;right:0;top:40px;text-align:center}
  .footer-nav a{color:#fff;text-decoration:none;font-size:15px;margin:0 7px}
  .footer-nav a.current{text-decoration:underline}
  .footer-brand{position:absolute;right:24px;top:38px;display:flex;align-items:center;gap:8px;color:#9a9a9a;font-size:14px;font-weight:700}
  .footer-brand i{width:22px;height:22px;background:#9a9a9a;display:block}
  .copyright{position:absolute;left:0;right:0;top:80px;text-align:center;font-size:10px;color:var(--footer-text)}
</style>
</head>
<body>
  <header>
    <div class="masthead" role="img" aria-label="Black and white photograph of smooth pebbles on a shore"></div>
    <div class="masthead-rule"></div>
    <div class="brand"><span class="brand-mark"></span><span class="brand-name">Theo Brandvik Photography</span></div>
    <nav class="main-nav">
      <a class="current" href="#">Home</a><a href="#">About</a><a href="#">Portfolio</a><a href="#">Clients Area</a><a href="#">Links</a><a href="#">Contact</a>
    </nav>
    <p class="slogan">Here <em>could</em> be you slogan!</p>
  </header>

  <main>
    <section class="panel intro">
      <div class="feature" role="img" aria-label="Black and white photograph of two fishermen in a small boat on calm water">
        <p class="feature-caption">RANDOM PHOTO, ALBUM or PHOTO SERIES</p>
      </div>
      <div class="welcome">
        <h2>Welcome to my site!</h2>
        <p>Lorem ipsum dolor sit amet, consectetur adipiscing elit. Pellentesque lobortis condimentum ipsum, non dictum ipsum malesuada ut. Class aptent taciti sociosqu ad litora torquent per conubia nostra, per inceptos himenaeos. Aenean ullamcorper rhoncus convallis. Sed laoreet elementum.</p>
        <p class="signature">Theo Brandvik</p>
      </div>
    </section>

    <section class="panel latest">
      <h2>Latest Photos</h2>
      <div class="thumb" style="left:40px"><div class="thumb-frame">photo thumbnail</div><span>Name of photo</span></div>
      <div class="thumb" style="left:222px"><div class="thumb-frame">photo thumbnail</div><span>Name of photo</span></div>
      <div class="thumb" style="left:410px"><div class="thumb-frame">photo thumbnail</div><span>Name of photo</span></div>
    </section>

    <section class="panel about">
      <h2>About me</h2>
      <div class="portrait">your portrait</div>
      <p>Lorem ipsum dolor sit amet, consectetur adipiscing elit. Pellentesque lobortis condimentum ipsum, non dictum ipsum malesuada ut. Class aptent taciti sociosqu ad litora torquent per conubia nostra, per inceptos himenaeos. Aenean ullamcorper rhoncus convallis. Sed laoreet elementu.<br><a href="#">[more]</a></p>
    </section>
  </main>

  <footer class="site-footer">
    <div class="elsewhere"><strong>Elsewhere...</strong><small>Snapfeed | Artloft | Linkpile | Friendbook</small></div>
    <nav class="footer-nav">
      <a class="current" href="#">Home</a><a href="#">About</a><a href="#">Portfolio</a><a href="#">Clients Area</a><a href="#">Links</a><a href="#">Contact</a>
    </nav>
    <div class="footer-brand"><i></i>Theo Brandvik</div>
    <p class="copyright">Copyright © theobrandvik-photography, 2010. All Rights Reserved.</p>
  </footer>
</body>
</html>
```